Design business card for Bright Harbour Coaching!

I am a personal development coach (like a life coach) and corporate trainer and need a professionally designed double sided business card.

It needs to contain the business logo (I'm happy for the designer to choose the layout of the logo as I am still working out the best option myself) and the following information:

Corinne Vashti
Personal Development Coach and Trainer

+61 (0)452 918 637 (written that way)
corinne@bright-harbour.example

www.bright-harbour.example

```html
<!DOCTYPE html>
<html lang="en">
<head>
<meta charset="utf-8">
<title>Bright Harbour Coaching – Business Card</title>
<link href="https://fonts.googleapis.com/css2?family=Cinzel:wght@400&family=Noto+Serif:ital,wght@0,400;1,400&display=swap" rel="stylesheet">
<style>
  :root {
    --backdrop: #cbcbcb;
    --card: #fafafa;
    --teal: #1f7f86;
    --teal-mark: #14919c;
    --ink: #5a5a5a;
    --muted: #6b6b6b;
    --rule: #e2e2e2;
  }
  html, body {
    margin: 0;
    padding: 0;
    width: 1193px;
    height: 1200px;
    overflow: hidden;
    background: var(--backdrop);
  }
  .sheet { position: relative; width: 1193px; height: 1200px; }
  .card {
    position: absolute;
    left: 256px;
    width: 687px;
    height: 415px;
    background: var(--card);
    overflow: hidden;
  }
  .card--front { top: 173px; }
  .card--back { top: 617px; }

  .brand-dot {
    position: absolute;
    border-radius: 50%;
    background: var(--teal-mark);
  }
  .brand-name {
    position: absolute;
    margin: 0;
    font-family: "Cinzel", serif;
    font-weight: 400;
    color: var(--ink);
    white-space: nowrap;
    text-align: center;
  }
  .card--front .brand-dot { width: 92px; height: 92px; left: 298px; top: 110px; }
  .card--front .brand-name { left: 0; right: 0; top: 245px; font-size: 34px; letter-spacing: 1px; }

  .card--back .brand-dot { width: 84px; height: 84px; left: 132px; top: 130px; }
  .card--back .brand-name { left: 30px; width: 288px; top: 265px; font-size: 19px; letter-spacing: 0.5px; }

  .divider {
    position: absolute;
    left: 322px;
    top: 55px;
    width: 1px;
    height: 275px;
    background: var(--rule);
  }
  .person {
    position: absolute;
    left: 357px;
    top: 116px;
    font-family: "Noto Serif", serif;
  }
  .person__name {
    margin: 0;
    font-size: 21px;
    font-weight: 400;
    color: var(--teal);
  }
  .person__role {
    margin: 8px 0 0;
    font-size: 14.5px;
    font-style: italic;
    line-height: 19px;
    color: var(--muted);
  }
  .contacts {
    position: absolute;
    left: 352px;
    top: 220px;
    margin: 0;
    padding: 0;
    list-style: none;
    font-family: "Noto Serif", serif;
    font-size: 16px;
    color: var(--muted);
  }
  .contacts li {
    display: flex;
    align-items: center;
    height: 27.5px;
  }
  .contacts svg { width: 17px; height: 17px; margin-right: 18px; fill: var(--teal); }
</style>
</head>
<body>
<main class="sheet">
  <section class="card card--front" aria-label="Card front">
    <span class="brand-dot" aria-hidden="true"></span>
    <h1 class="brand-name">Bright Harbour Coaching</h1>
  </section>

  <section class="card card--back" aria-label="Card back">
    <span class="brand-dot" aria-hidden="true"></span>
    <p class="brand-name">Bright Harbour Coaching</p>
    <span class="divider" aria-hidden="true"></span>
    <div class="person">
      <h2 class="person__name">Corinne Vashti</h2>
      <p class="person__role">Personal Development Coach<br>and Trainer</p>
    </div>
    <ul class="contacts">
      <li>
        <svg viewBox="0 0 20 20" aria-hidden="true"><path d="M2 6c0-2 3-3 8-3s8 1 8 3v2h-4V6.5c-1-.5-2.5-.7-4-.7s-3 .2-4 .7V8H2z"/><path d="M5 9h10l2 8H3z"/><circle cx="10" cy="13" r="2" fill="#fafafa"/></svg>
        +61 (0)452 918 637
      </li>
      <li>
        <svg viewBox="0 0 20 20" aria-hidden="true"><path d="M2 4h16v12H2z"/><path d="M2.5 4.5 10 11l7.5-6.5" fill="none" stroke="#fafafa" stroke-width="1.5"/></svg>
        corinne@bright-harbour.example
      </li>
      <li>
        <svg viewBox="0 0 20 20" aria-hidden="true"><circle cx="10" cy="10" r="8"/><path d="M2 10h16M10 2v16M4 5.5h12M4 14.5h12" stroke="#fafafa" stroke-width="1" fill="none"/><ellipse cx="10" cy="10" rx="3.5" ry="8" fill="none" stroke="#fafafa" stroke-width="1"/></svg>
        www.bright-harbour.example
      </li>
    </ul>
  </section>
</main>
</body>
</html>
```